Business Card Design

We offer full auto repair and auto customization from custom wheels to lift kits and drop kits we do it all. I want something that grabs your attention from the start but nothing flashy i am more of a clean crisp modern kinda of guy. I plan on using the design on my business cards and my main business sign .
Updates
I have up loaded an image of my currant business card designed by me , I would like to improve on it
Target Market(s)
20-35 male and female
Industry/Entity Type
Business
Contact Information for Business Card
Corvello Wheel Works
48362 1/2 Parkfield rd
Houston TX, 77070
Manager: Dorian Walsh
P:555-214-7730
F:555-214-7781
Email:Dorian@corvellowheelandgarage.example
website:Corvellowheelandgarage.example
Look and feel

```html
<!DOCTYPE html>
<html lang="en">
<head>
<meta charset="utf-8">
<title>Corvello Wheel Works — Business Card</title>
<link rel="stylesheet" href="https://fonts.googleapis.com/css2?family=Josefin+Sans:wght@400;600&display=swap">
<style>
  :root {
    --card-base: #f3f3f3;
    --card-stripe: rgba(0, 0, 0, 0.025);
    --edge-bar: #4f4f4f;
    --ink: #2e2e2e;
    --ink-soft: #3a3a3a;
    --track-dark: #3c3c3c;
    --track-mid: #8a8a8a;
  }
  * { margin: 0; padding: 0; box-sizing: border-box; }
  html, body {
    width: 1200px;
    height: 702px;
    overflow: hidden;
    background: var(--card-base);
  }
  .card {
    position: relative;
    width: 1200px;
    height: 702px;
    overflow: hidden;
    background:
      radial-gradient(ellipse at 30% 40%, rgba(255,255,255,0.7), rgba(255,255,255,0) 70%),
      repeating-linear-gradient(135deg, var(--card-stripe) 0 2px, transparent 2px 6px),
      var(--card-base);
    font-family: "Josefin Sans", sans-serif;
  }
  .edge-bar {
    position: absolute;
    left: 0;
    top: 0;
    width: 13px;
    height: 100%;
    background: var(--edge-bar);
  }
  .tire-track {
    position: absolute;
    left: 61px;
    top: 491px;
    width: 480px;
    height: 149px;
    background:
      repeating-linear-gradient(90deg, rgba(0,0,0,0.18) 0 9px, transparent 9px 20px),
      linear-gradient(90deg, var(--track-dark) 0%, var(--track-dark) 55%, var(--track-mid) 78%, rgba(138,138,138,0) 100%);
    -webkit-mask-image: linear-gradient(90deg, #000 0%, #000 60%, transparent 100%);
            mask-image: linear-gradient(90deg, #000 0%, #000 60%, transparent 100%);
    opacity: 0.85;
  }
  .business-name {
    position: absolute;
    left: 543px;
    top: 494px;
    font-size: 42px;
    font-weight: 400;
    letter-spacing: 0.5px;
    text-transform: uppercase;
    color: var(--ink);
    text-shadow: 2px 3px 3px rgba(0,0,0,0.3);
    white-space: nowrap;
  }
  .tagline {
    position: absolute;
    left: 701px;
    top: 555px;
    font-size: 19px;
    font-weight: 400;
    text-transform: uppercase;
    color: var(--ink-soft);
    text-shadow: 1px 2px 2px rgba(0,0,0,0.3);
    white-space: nowrap;
  }
</style>
</head>
<body>
  <main class="card">
    <div class="edge-bar"></div>
    <div class="tire-track" role="img" aria-label="Tire tread track fading to the right"></div>
    <h1 class="business-name">Corvello Wheel Works</h1>
    <p class="tagline">Full auto repair and customization</p>
  </main>
</body>
</html>
```